Vegan Alfredo Sauce Label Design for Brambleway Pantry Co

We are a food co. committed to making vegan food more accessible to people who want to eat healthier. Our first line of product is vegan Alfredo sauce.
We have 3 flavors:
- Garlic
- Pesto
- Lemony Artichoke
The current project is the design for the first flavor: garlic. However, we would like a template that would translate well to other flavors, so they look like a family of products.
These will be in standard 16 oz jars. The whole label will be approx 6cm x 24cm, but the front visual space is approx 6cm x 10cm. The rest will be nutritional labeling and copy about the company.
We also need a stamp or font- based logo that says Brambleway Pantry Co. (or lower case: brambleway pantry co.), the name of the company.
The picture (attached) of Plantbased Nacho Dip is the closest to what we are going for. Because the sauce is creamy white, a colorful background with off-white font will be best.
We currently have a website, although we are doing a brand over-haul (hence, this posting) www.bramblewaypantryco.example. If the designer is a good fit, we have several more projects, in line.
Other brands we love: Tidewell Grocers, Marlow Ridge Provisions, Pulp Poured Daily.
The final brand should communicate hip, natural and health.
And personally, I love design that is clever and somehow makes me smile.
Target Market(s)
Vegans, vegetarians, and people with common food allergies - all ages.
Young, hip families.
Industry/Entity Type
It Company
Requirements
Must have
- Copy:
Vegan Alfredo or Vegan Alfredo Sauce
Garlic
Brambleway Pantry or Brambleway Pantry Co
16 oz
Nice to have
- May include copy:
Gluten-Free Soy-Free Nut-Free
Should not have
- Neon colors

```html
<!DOCTYPE html>
<html lang="en">
<head>
<meta charset="utf-8">
<title>Brambleway Pantry – Vegan Alfredo Sauce, Garlic</title>
<link rel="stylesheet" href="https://fonts.googleapis.com/css2?family=Caladea&family=Coustard:wght@900&display=swap">
<style>
  :root {
    --page: #ffffff;
    --label-top: #3a8fae;
    --label-mid: #8a8a9e;
    --label-body: #b57f89;
    --label-foot: #8c8aa0;
    --cream: #f8e2d9;
    --flavor: #e7e9b9;
    --flavor-shadow: rgba(90, 40, 50, 0.55);
    --vegan: #a8f0a0;
    --alfredo: #f5e86c;
    --sauce: #f7c9ae;
    --bulb-light: #f4eef2;
    --bulb-shade: #c9a9c2;
  }
  * { margin: 0; padding: 0; box-sizing: border-box; }
  html, body {
    width: 1188px;
    height: 1200px;
    overflow: hidden;
    background: var(--page);
  }
  .canvas {
    position: relative;
    width: 1188px;
    height: 1200px;
  }
  .label {
    position: absolute;
    left: 81px;
    top: 80px;
    width: 1009px;
    height: 1034px;
    background: linear-gradient(
      to bottom,
      var(--label-top) 0%,
      var(--label-mid) 20%,
      var(--label-body) 34%,
      var(--label-body) 94%,
      var(--label-foot) 100%
    );
    font-family: "Caladea", Georgia, serif;
  }
  .brand-name {
    position: absolute;
    left: 0;
    right: 0;
    top: 155px;
    text-align: center;
    font-size: 72px;
    font-weight: 400;
    color: var(--cream);
    letter-spacing: 1px;
  }
  .product-line {
    position: absolute;
    left: 0;
    right: 0;
    top: 312px;
    text-align: center;
    font-family: "Coustard", "Cooper Black", serif;
    font-weight: 900;
    font-size: 45px;
    word-spacing: 14px;
  }
  .product-line .vegan { color: var(--vegan); }
  .product-line .alfredo { color: var(--alfredo); }
  .product-line .sauce { color: var(--sauce); }
  .flavor {
    position: absolute;
    left: 0;
    right: 0;
    top: 420px;
    text-align: center;
    font-family: "Coustard", "Cooper Black", serif;
    font-weight: 900;
    font-size: 176px;
    line-height: 1;
    color: var(--flavor);
    text-shadow: 5px 6px 6px var(--flavor-shadow);
  }
  .flavor-art {
    position: absolute;
    left: 144px;
    top: 667px;
    width: 236px;
    height: 253px;
    border-radius: 46% 46% 44% 44% / 58% 58% 40% 40%;
    background: radial-gradient(ellipse at 45% 55%, var(--bulb-light) 0%, var(--bulb-light) 45%, var(--bulb-shade) 100%);
  }
  .allergen-claims {
    position: absolute;
    left: 445px;
    top: 790px;
    display: flex;
    align-items: center;
    color: var(--cream);
  }
  .allergen-list {
    list-style: none;
    font-size: 37px;
    line-height: 47px;
  }
  .allergen-list .soy { letter-spacing: 8px; }
  .allergen-list .nut { letter-spacing: 6px; }
  .free-word {
    margin-left: 20px;
    font-size: 150px;
    line-height: 1;
    transform: scaleX(0.78);
    transform-origin: left center;
    letter-spacing: 2px;
  }
  .net-weight {
    position: absolute;
    left: 449px;
    top: 1004px;
    font-size: 20px;
    color: var(--cream);
  }
</style>
</head>
<body>
<div class="canvas">
  <section class="label">
    <h1 class="brand-name">Brambleway Pantry</h1>
    <p class="product-line">
      <span class="vegan">Vegan</span>
      <span class="alfredo">Alfredo</span>
      <span class="sauce">Sauce</span>
    </p>
    <h2 class="flavor">Garlic</h2>
    <div class="flavor-art" role="img" aria-label="Illustration of a white garlic bulb"></div>
    <div class="allergen-claims">
      <ul class="allergen-list">
        <li class="gluten">Gluten</li>
        <li class="soy">Soy</li>
        <li class="nut">Nut</li>
      </ul>
      <span class="free-word">FREE</span>
    </div>
    <p class="net-weight">16 oz</p>
  </section>
</div>
</body>
</html>
```